Halworth Builds, Carpentry Services

Business card for carpentry business in the Sunshine Coast.

Business card layout required using logo provided - provided both PDF copy and AI. Please let me know if you would like a the files for the logo symbol and text by itself.

Business Colours are grey, blue and white. The font colours codes for this design are Blue Hex # 00B4E6 and Hex # 39393B for the gray colour.

FYI font for logo is Gotham Bold.

Preference for a clean and striking layout that is simple and elegant.

Target Market(s)

Young Families, retirees, young couples requiring assistance with small to medium works/renovations on the Sunshine Coast.

Industry/Entity Type

Construction

Contact Information for Business Card

Dean Halworth
Carpenter
0481356027
dean@halworthbuilds.com.au
Kellbrook, Seabright Coast
RHLA Licensed Carpenter (In smaller font)

Font styles to use
Sans Serif

Colors

Designer to choose colors to be used in the design.

Requirements
Must have
• Logo provided must appear on the card, preferably on one side of the card by itself with the text on the alternate side
Nice to have
• Text on the other side of card, maybe grey background and white font here but happy for the designer to provide ideas here.
Should not have
• Use of other colours, other than the ones provided - white, grey and blue. Black optional.

```html
<!DOCTYPE html>
<html lang="en">
<head>
<meta charset="utf-8">
<title>Halworth Builds – Business Card</title>
<link href="https://fonts.googleapis.com/css2?family=Montserrat:wght@700&family=Roboto:wght@400;500&display=swap" rel="stylesheet">
<style>
  :root {
    --blue: #00B4E6;
    --grey: #39393B;
    --white: #FFFFFF;
    --stage: #E6E7E9;
    --muted: #5A5A5D;
  }
  * { margin: 0; padding: 0; box-sizing: border-box; }
  html, body { width: 1200px; height: 901px; overflow: hidden; }
  body { background: var(--stage); position: relative; font-family: "Roboto", Arial, sans-serif; }

  .card {
    position: absolute;
    width: 620px; height: 379px;
    overflow: hidden;
    box-shadow: 0 10px 30px rgba(0,0,0,0.18);
  }
  .card--front { left: 60px; top: 60px; background: var(--blue); }
  .card--back  { left: 520px; top: 462px; background: var(--white); }

  .brand { display: flex; align-items: center; gap: 18px; position: absolute; white-space: nowrap; }
  .brand__mark { width: 46px; height: 46px; flex: none; }
  .brand__name {
    font-family: "Montserrat", Arial, sans-serif;
    font-weight: 700; font-size: 36px; letter-spacing: 1px;
    text-transform: uppercase; line-height: 1; white-space: nowrap;
  }
  .card--front .brand { left: 50%; top: 50%; transform: translate(-50%, -50%); }
  .card--front .brand__mark { background: var(--white); }
  .card--front .brand__name { color: var(--white); }

  .back__sweep { position: absolute; left: 0; top: 0; width: 620px; height: 379px; }

  .person { position: absolute; right: 40px; top: 34px; text-align: right; }
  .person__name {
    font-family: "Montserrat", Arial, sans-serif; font-weight: 700;
    font-size: 21px; color: var(--blue); text-transform: uppercase; letter-spacing: 0.3px;
  }
  .person__role { font-size: 14px; color: var(--muted); margin-top: 3px; }

  .card--back .brand { left: 150px; top: 152px; }
  .card--back .brand__mark { background: var(--blue); }
  .card--back .brand__name { color: var(--grey); font-size: 32px; }

  .contact {
    position: absolute; left: 210px; top: 236px;
    padding-left: 18px; border-left: 2px solid var(--blue);
    color: var(--grey); font-size: 15px; line-height: 1.45;
  }
  .contact__licence { color: var(--blue); font-size: 12.5px; margin-bottom: 6px; }
  .contact__row { display: flex; align-items: center; gap: 8px; }
  .contact__icon { width: 13px; height: 13px; flex: none; fill: var(--blue); }
</style>
</head>
<body>

  <section class="card card--front" aria-label="Card front">
    <div class="brand">
      <span class="brand__mark"></span>
      <span class="brand__name">Halworth Builds</span>
    </div>
  </section>

  <section class="card card--back" aria-label="Card back">
    <svg class="back__sweep" viewBox="0 0 620 379" aria-hidden="true">
      <path d="M0 0 H440 Q170 55 0 215 Z" fill="var(--blue)"/>
      <path d="M440 0 Q170 55 0 215" fill="none" stroke="var(--grey)" stroke-width="7"/>
    </svg>

    <div class="person">
      <div class="person__name">Dean Halworth</div>
      <div class="person__role">Carpenter</div>
    </div>

    <div class="brand">
      <span class="brand__mark"></span>
      <span class="brand__name">Halworth Builds</span>
    </div>

    <div class="contact">
      <div class="contact__location">Kellbrook, Seabright Coast</div>
      <div class="contact__licence">RHLA Licensed Carpenter</div>
      <div class="contact__row">
        <svg class="contact__icon" viewBox="0 0 24 24" aria-hidden="true"><path d="M6.6 10.8a15.1 15.1 0 0 0 6.6 6.6l2.2-2.2a1 1 0 0 1 1-.25 11.4 11.4 0 0 0 3.6.57 1 1 0 0 1 1 1V20a1 1 0 0 1-1 1A17 17 0 0 1 3 4a1 1 0 0 1 1-1h3.5a1 1 0 0 1 1 1c0 1.250.2 2.45.57 3.6a1 1 0 0 1-.25 1z"/></svg>
        <span>0481356027</span>
      </div>
      <div class="contact__row">
        <svg class="contact__icon" viewBox="0 0 24 24" aria-hidden="true"><path d="M2 5h20v14H2z M2 5l10 8 10-8" fill="var(--blue)" stroke="var(--white)" stroke-width="1.5"/></svg>
        <span>dean@halworthbuilds.com.au</span>
      </div>
    </div>
  </section>

</body>
</html>
```